Hospital website for specialized hospital on Eye care

Dear ,

I want create hospital website template slimier to this
(http://www.plinthvane.com/design/7720581)

and the banner similer to this site 4466502 design

3 pages ( Home , Overview page , left menu page)

the color should be fit with our logo ( www.qorvale.med.sa) - no green color pleaase.

Also i would like from you to design one banner image for the home page , the file of the image can be locate on the below site link

www.qorvale.med.sa

Target Market(s)

healthcare

Industry/Entity Type

Hospital

Coding

Coded - Design and coding required

Number of Pages Required

3 page

Requirements
Must have
• as in the attached and current website layout conent www.qorvale.med.sa
Nice to have
• The General Layout shuld be like 4439013 and the banner like this 4466502
Should not have
• no specific

```html
<!DOCTYPE html>
<html lang="en">
<head>
<meta charset="utf-8">
<title>Qorvale Eye Specialist Hospital</title>
<link href="https://fonts.googleapis.com/css2?family=Open+Sans:wght@400;600;700&display=swap" rel="stylesheet">
<style>
:root{
  --brand-dark:#163a5c;
  --brand:#1f5685;
  --brand-mid:#2a6a9e;
  --brand-light:#3a80b8;
  --gold:#e3ad18;
  --page:#e7e8e9;
  --panel:#ffffff;
  --text:#444;
  --muted:#888;
  --line:#d9dce0;
}
*{box-sizing:border-box;margin:0;padding:0}
html,body{width:709px;height:1200px;overflow:hidden}
body{font-family:"Open Sans",Arial,sans-serif;color:var(--text);background:var(--page);position:relative}
.abs{position:absolute}

/* header */
.site-header{left:0;top:0;width:709px;height:90px;background:var(--panel)}
.brand{left:20px;top:14px;display:flex;align-items:center;gap:8px}
.brand-mark{width:30px;height:30px;border-radius:50%;background:var(--brand)}
.brand-name{font-size:9px;font-weight:600;color:var(--brand);line-height:1.25;width:130px}
.utility-nav{right:22px;top:9px;display:flex;gap:10px;font-size:6.5px;color:var(--muted)}
.main-nav{right:22px;top:40px;display:flex;gap:16px;font-size:9.5px;color:#555}

/* hero */
.hero-menu{left:0;top:90px;width:236px;height:262px;background:linear-gradient(180deg,var(--brand-mid),var(--brand-dark))}
.hero-item{position:absolute;left:22px;display:flex;align-items:center;gap:10px;color:#fff;font-size:9px}
.hero-icon{width:16px;height:16px;border-radius:50%;background:rgba(255,255,255,.25);display:flex;align-items:center;justify-content:center}
.hero-divider{position:absolute;left:22px;width:190px;height:1px;background:rgba(255,255,255,.18)}
.search-label{position:absolute;left:22px;top:190px;color:#fff;font-size:7.5px}
.search-input{position:absolute;left:22px;top:204px;width:118px;height:16px;background:#fff;border-radius:2px;font-size:6px;color:#aaa;padding:4px 5px}
.search-btn{position:absolute;left:22px;top:228px;width:40px;height:14px;background:var(--gold);color:#fff;font-size:6.5px;font-weight:700;text-align:center;line-height:14px}
.hero-photo{left:236px;top:90px;width:473px;height:262px;background:linear-gradient(120deg,#e1e9ef 0%,#bccfdc 45%,#82a4bd 75%,#4f7896 100%)}
.hero-caption{left:283px;top:224px;width:224px;height:94px;background:rgba(255,255,255,.88);padding:10px 12px}
.hero-caption h2{font-size:15px;font-weight:600;color:var(--brand)}
.hero-caption p{font-size:6.5px;color:#666;margin-top:5px;line-height:1.45}
.dots{display:flex;gap:4px;margin-top:7px}
.dots i{width:5px;height:5px;border-radius:50%;background:#bbb}
.dots i.on{background:var(--brand)}

/* audience tiles */
.audience-band{left:0;top:352px;width:709px;height:103px;background:#f4f5f6}
.tiles{left:59px;top:365px;width:590px;display:flex;justify-content:space-between}
.tile{width:84px;height:72px;background:var(--brand-mid);border-radius:2px;overflow:hidden;display:flex;flex-direction:column}
.tile-icon{flex:1;display:flex;align-items:center;justify-content:center;background:var(--brand-light)}
.tile-label{height:22px;background:var(--brand);color:#fff;font-size:9px;text-align:center;line-height:22px}

/* panels */
.panel{background:var(--panel);box-shadow:0 1px 2px rgba(0,0,0,.08)}
.panel-head{height:26px;line-height:26px;padding-left:10px;font-size:10px;color:#333;border-bottom:2px solid var(--brand)}
.panel-head.solid{background:var(--brand);color:#fff;border:none}

.news{left:59px;top:478px;width:361px;height:258px}
.news-photo{position:absolute;left:10px;top:36px;width:168px;height:96px;background:linear-gradient(135deg,#d2dfe9,#91aec4)}
.news-title{position:absolute;left:10px;top:138px;width:170px;font-size:8px;color:var(--brand);font-weight:600;line-height:1.3}
.news-date{position:absolute;left:10px;top:162px;font-size:6px;color:var(--muted)}
.news-text{position:absolute;left:10px;top:173px;width:170px;font-size:6px;color:#777;line-height:1.5}
.news-side{position:absolute;left:190px;width:160px;display:flex;gap:7px}
.news-thumb{width:52px;height:40px;flex:none;background:linear-gradient(135deg,#d9e3eb,#9fb9cc)}
.news-side p{font-size:6px;color:#666;line-height:1.45}
.news .dots{position:absolute;left:170px;top:238px}

.events{left:432px;top:478px;width:218px;height:100px}
.event-item{display:flex;gap:6px;padding:7px 10px 0}
.event-item .arrow{color:var(--brand);font-size:8px;line-height:10px}
.event-item b{display:block;font-size:7.5px;font-weight:600;color:var(--brand);line-height:1.3}
.event-item small{display:block;font-size:6px;color:var(--muted);line-height:1.3;margin-top:2px}

.poll{left:432px;top:586px;width:218px;height:70px}
.poll-q{font-size:7.5px;color:#444;padding:8px 10px 5px}
.poll-row{display:flex;align-items:center;gap:5px;padding-left:10px;font-size:6.5px}
.radio{width:7px;height:7px;border-radius:50%;border:1px solid #999}
.poll-btn{background:var(--brand);color:#fff;font-size:6.5px;padding:2px 5px;margin-left:4px}

.upcoming{left:59px;top:770px;width:591px;height:176px}
.tabs{display:flex;border-bottom:2px solid var(--brand)}
.tab{height:24px;line-height:24px;padding:0 12px;font-size:9.5px;color:#555}
.tab.active{background:var(--brand);color:#fff}
.event-cards{display:flex;gap:11px;padding:12px 10px 0}
.card{width:134px}
.card-photo{height:80px;background:linear-gradient(135deg,#dde6ed,#91aec2)}
.card b{display:block;font-size:7.5px;font-weight:600;color:var(--brand);margin-top:6px}
.card small{font-size:6px;color:var(--muted)}

.awards{left:59px;top:990px;width:361px;height:130px}
.badges{display:flex;gap:22px;align-items:center;padding:28px 18px}
.badge{width:52px;height:42px;background:#d6dadf;border-radius:3px}
.badge.round{width:42px;border-radius:50%}

.contact{left:432px;top:990px;width:218px;height:130px}
.contact-body{padding:12px 10px;font-size:7px;line-height:1.7;color:#555}
.contact-body strong{display:block;font-size:11px;font-weight:600;color:#333;margin-bottom:4px}

.site-footer{left:0;top:1145px;width:709px;height:55px;background:var(--brand-dark)}
.footer-nav{position:absolute;left:22px;top:12px;display:flex;gap:12px;font-size:6.5px;color:#dde6ee}
.copyright{position:absolute;left:22px;top:27px;font-size:6px;color:#a6bacb}
.footer-social{position:absolute;right:22px;top:12px;display:flex;gap:6px}
.footer-social i{width:8px;height:8px;border-radius:50%;background:#dde6ee}
</style>
</head>
<body>

<header class="site-header abs">
  <div class="brand abs"><span class="brand-mark"></span><span class="brand-name">Qorvale Eye Specialist Hospital</span></div>
  <nav class="utility-nav abs"><span>Careers</span><span>Contact Us</span><span>Locations</span><span>Gallery</span><span>Search</span></nav>
  <nav class="main-nav abs"><span>Home</span><span>About</span><span>Patients and Visitors</span><span>Professionals</span><span>E-Services</span></nav>
</header>

<section class="hero-menu abs">
  <div class="hero-item" style="top:36px"><span class="hero-icon"><svg width="8" height="8" viewBox="0 0 8 8"><path d="M1 4h6M4 1v6" stroke="#fff" stroke-width="1.4"/></svg></span>Before Your Visit</div>
  <div class="hero-divider" style="top:63px"></div>
  <div class="hero-item" style="top:73px"><span class="hero-icon"><svg width="8" height="8" viewBox="0 0 8 8"><rect x="1" y="1.5" width="6" height="5.5" fill="none" stroke="#fff"/></svg></span>Schedule A Lab Test</div>
  <div class="hero-divider" style="top:100px"></div>
  <div class="hero-item" style="top:110px"><span class="hero-icon"><svg width="8" height="8" viewBox="0 0 8 8"><rect x="0.5" y="2" width="7" height="4.5" fill="none" stroke="#fff"/></svg></span>Online Bill Pay</div>
  <div class="hero-divider" style="top:137px"></div>
  <div class="hero-item" style="top:147px"><span class="hero-icon"><svg width="8" height="8" viewBox="0 0 8 8"><path d="M4 7L1 4a1.6 1.6 0 013-2 1.6 1.6 0 013 2z" fill="#fff"/></svg></span>Support Our Work</div>
  <div class="search-label">Do you Want To Learn About A Conditions</div>
  <div class="search-input">Enter Key Word Here</div>
  <div class="search-btn">SEARCH</div>
</section>
<div class="hero-photo abs" role="img" aria-label="Hospital corridor with medical staff in scrubs"></div>
<div class="hero-caption abs">
  <h2>The World Health Day</h2>
  <p>World Health Day focuses this year on the risks of high blood pressure for heart and eye health.</p>
  <div class="dots"><i class="on"></i><i></i><i></i></div>
</div>

<div class="audience-band abs"></div>
<div class="tiles abs">
  <div class="tile"><div class="tile-icon"><svg width="18" height="18" viewBox="0 0 18 18"><circle cx="9" cy="6" r="3.5" fill="#fff"/><path d="M2 17a7 7 0 0114 0z" fill="#fff"/></svg></div><div class="tile-label">Patient</div></div>
  <div class="tile"><div class="tile-icon"><svg width="18" height="18" viewBox="0 0 18 18"><rect x="3" y="2" width="12" height="15" fill="none" stroke="#fff" stroke-width="1.6"/><path d="M6 7h6M6 10h6M6 13h4" stroke="#fff" stroke-width="1.4"/></svg></div><div class="tile-label">Employee</div></div>
  <div class="tile"><div class="tile-icon"><svg width="18" height="18" viewBox="0 0 18 18"><rect x="2" y="6" width="14" height="10" fill="#fff"/><rect x="6" y="3" width="6" height="3" fill="none" stroke="#fff" stroke-width="1.4"/></svg></div><div class="tile-label">Vendor</div></div>
  <div class="tile"><div class="tile-icon"><svg width="18" height="18" viewBox="0 0 18 18"><path d="M1 7l8-4 8 4-8 4z" fill="#fff"/><path d="M5 9v4c2 2 6 2 8 0V9" fill="none" stroke="#fff" stroke-width="1.4"/></svg></div><div class="tile-label">Trainee</div></div>
  <div class="tile"><div class="tile-icon"><svg width="18" height="18" viewBox="0 0 18 18"><path d="M2 7l7-4 7 4z" fill="#fff"/><path d="M4 8v6M7.5 8v6M10.5 8v6M14 8v6M2 16h14" stroke="#fff" stroke-width="1.5"/></svg></div><div class="tile-label">Government</div></div>
  <div class="tile"><div class="tile-icon"><svg width="18" height="18" viewBox="0 0 18 18"><rect x="2" y="5" width="14" height="11" fill="none" stroke="#fff" stroke-width="1.6"/><path d="M7 5V3h4v2M2 10h14" stroke="#fff" stroke-width="1.4"/></svg></div><div class="tile-label">Career</div></div>
</div>

<section class="news panel abs">
  <div class="panel-head">Latest News</div>
  <div class="news-photo" role="img" aria-label="Doctors in an operating room"></div>
  <div class="news-title">The World Health Day 2015 under the motto "High Blood Pressure"</div>
  <div class="news-date">20 Jul 2015</div>
  <div class="news-text">Our hospital marked the day with free eye checks and talks on pressure care for visitors.</div>
  <div class="news-side" style="top:36px"><div class="news-thumb" role="img" aria-label="Clinic news photo"></div><p>Hospital team joins the national screening week for children.</p></div>
  <div class="news-side" style="top:86px"><div class="news-thumb" role="img" aria-label="Hospital news photo"></div><p>New retina unit opens with extended hours for patients.</p></div>
  <div class="news-side" style="top:136px"><div class="news-thumb" role="img" aria-label="Medical staff news photo"></div><p>American Association of Eye Care Centers grants full award.</p></div>
  <div class="dots"><i class="on"></i><i></i><i></i></div>
</section>

<section class="events panel abs">
  <div class="panel-head solid">Current Events</div>
  <div class="event-item"><span class="arrow">›</span><div><b>21st Annual Nursing Symposium</b><small>20 Jul 2015</small></div></div>
  <div class="event-item"><span class="arrow">›</span><div><b>3rd Diagnostic Imaging Symposium in Ophthalmology</b><small>20 Jul 2015</small></div></div>
</section>

<section class="poll panel abs">
  <div class="panel-head">Opinion Polls</div>
  <div class="poll-q">Do you like the new website design?</div>
  <div class="poll-row"><span class="radio"></span>Yes <span class="radio"></span>No <span class="poll-btn">Submit</span></div>
</section>

<section class="upcoming panel abs">
  <div class="tabs"><div class="tab active">Upcoming Events</div><div class="tab">Past Events</div></div>
  <div class="event-cards">
    <div class="card"><div class="card-photo" role="img" aria-label="Group of hospital staff"></div><b>Lorem ipsum dolor sit amet</b><small>20 Jul 2015</small></div>
    <div class="card"><div class="card-photo" role="img" aria-label="Hospital building exterior"></div><b>Lorem ipsum dolor sit amet</b><small>20 Jul 2015</small></div>
    <div class="card"><div class="card-photo" role="img" aria-label="Surgeon at work"></div><b>Lorem ipsum dolor sit amet</b><small>20 Jul 2015</small></div>
    <div class="card"><div class="card-photo" role="img" aria-label="Doctor with patient"></div><b>Lorem ipsum dolor sit amet</b><small>20 Jul 2015</small></div>
  </div>
</section>

<section class="awards panel abs">
  <div class="panel-head solid">Awards and Recognitions</div>
  <div class="badges"><span class="badge"></span><span class="badge round"></span><span class="badge round"></span><span class="badge"></span></div>
</section>

<section class="contact panel abs">
  <div class="panel-head solid">Contact Us</div>
  <div class="contact-body">
    <strong>P.O.Box: 4820 Riyadh 11500</strong>
    +966110005555 (Outside KSA) | 920004455<br>
    info@qorvale.med.sa<br>
    www.qorvale.med.sa
  </div>
</section>

<footer class="site-footer abs">
  <nav class="footer-nav"><span>Home</span><span>About</span><span>Patients and Visitors</span><span>Professionals</span><span>E-Services</span></nav>
  <div class="copyright">Copyright © 2015</div>
  <div class="footer-social"><i></i><i></i><i></i><i></i></div>
</footer>

</body>
</html>
```